Cigar Ring Design

we are working on a project, which is an eCommerce store for cigars, now instead of selling all kind of existing brands this project is based on a TabacoMillDepot concept where an outlet is linked to an actual Cigar factory,
so the cigar lines sold will come out under a TMD (TabacoMillDepot) brand consisting of various labels, (think Barney Cotter, Ochre Crest, Slate Crest etc) I had an idea for the Cigar Rings for this project, where I put TM in an O (circle) of which I made mock ups (see attachement), now I am not a designer, I am sure a real designer can come up with something more stylish and unique.

```html
<!DOCTYPE html>
<html lang="en">
<head>
<meta charset="utf-8">
<title>Tabaco Mill Depot – Cigar Rings</title>
<link rel="stylesheet" href="https://fonts.googleapis.com/css2?family=Red+Hat+Display:wght@400;500&display=swap">
<style>
  :root {
    --gold-dark: #5a3f12;
    --gold-mid: #a8832a;
    --gold-bright: #f5dc5a;
    --gold-warm: #d9b43c;
    --tab-gold: #c9a233;
    --ink: #2a1d05;
    --page: #ffffff;
    --gold-band: linear-gradient(90deg, var(--gold-dark) 0%, var(--gold-mid) 10%, var(--gold-bright) 20%, var(--gold-mid) 36%, var(--gold-warm) 50%, var(--gold-mid) 64%, var(--gold-bright) 80%, var(--gold-mid) 90%, var(--gold-dark) 100%);
  }
  * { box-sizing: border-box; margin: 0; padding: 0; }
  html, body { width: 960px; height: 1200px; overflow: hidden; background: var(--page); }
  .sheet { position: relative; width: 960px; height: 1200px; }
  .ring {
    position: absolute; left: 224px; width: 510px; height: 133px;
    box-shadow: 4px 6px 6px rgba(0,0,0,0.35);
    font-family: "Red Hat Display", sans-serif;
  }
  .ring--onyx   { top: 63px;  background: linear-gradient(90deg, #262626, #323233 50%, #2a2a2b 60%, #222223); }
  .ring--slate  { top: 250px; background: linear-gradient(90deg, #07034a, #1a1f74 50%, #1d2177 60%, #0a034d); }
  .ring--moss   { top: 437px; background: linear-gradient(90deg, #002e10, #005a29 35%, #007838 50%, #005a29 70%, #002a0d); }
  .ring--ochre  { top: 624px; background: linear-gradient(90deg, #7a0002, #9a0a12 30%, #d91e28 55%, #a80e16 78%, #5e0001); }
  .ring--pewter { top: 811px; background: linear-gradient(90deg, #8e8f93, #c9cacd 20%, #f4f4f5 38%, #d2d3d5 55%, #9fa0a4 78%, #535457); }
  .ring--amber  { top: 998px; background: linear-gradient(90deg, #a8833e, #c9ac6c 25%, #dcc98f 40%, #e6e7b4 62%, #e2dfa8 70%, #bc9c5e 100%); }

  .ring__strip { position: absolute; left: 0; width: 100%; height: 9px; background: var(--gold-band); }
  .ring__strip--top { top: 0; }
  .ring__strip--bottom { bottom: 0; }

  .ring__tab { position: absolute; left: 168px; width: 144px; height: 14px; }
  .ring__tab--top { top: 9px; }
  .ring__tab--bottom { bottom: 9px; }

  .ring__maker, .ring__line {
    position: absolute; left: 168px; width: 144px; text-align: center;
    color: var(--ink); font-size: 11px; letter-spacing: 0.2px; white-space: nowrap;
  }
  .ring__maker { top: 4px; font-weight: 400; }
  .ring__line { bottom: 4px; font-weight: 500; }

  .ring__seal {
    position: absolute; border-radius: 50%;
    background: radial-gradient(circle at 40% 35%, var(--gold-bright), var(--gold-warm) 45%, var(--gold-mid) 80%, var(--gold-dark));
    display: flex; align-items: center; justify-content: center;
    color: var(--ink); font-family: "Red Hat Display", sans-serif; font-weight: 500;
  }
  .ring__seal--main { left: 193px; top: 19px; width: 94px; height: 94px; font-size: 36px; box-shadow: 2px 3px 4px rgba(0,0,0,0.35); }
  .ring__seal--side { left: 455px; top: 42px; width: 48px; height: 48px; font-size: 18px; }
</style>
</head>
<body>
<svg width="0" height="0" style="position:absolute">
  <defs>
    <symbol id="tab-shape" viewBox="0 0 144 14" preserveAspectRatio="none">
      <path d="M0,0 H144 C136,0 134,14 126,14 H18 C10,14 8,0 0,0 Z" fill="#c9a233"/>
    </symbol>
  </defs>
</svg>
<main class="sheet">
  <section class="ring ring--onyx">
    <div class="ring__strip ring__strip--top"></div>
    <div class="ring__strip ring__strip--bottom"></div>
    <svg class="ring__tab ring__tab--top"><use href="#tab-shape"/></svg>
    <svg class="ring__tab ring__tab--bottom" style="transform:scaleY(-1)"><use href="#tab-shape"/></svg>
    <p class="ring__maker">TABACO MILL DEPOT</p>
    <div class="ring__seal ring__seal--main">TM</div>
    <div class="ring__seal ring__seal--side">TM</div>
    <p class="ring__line">ONYX CREST</p>
  </section>
  <section class="ring ring--slate">
    <div class="ring__strip ring__strip--top"></div>
    <div class="ring__strip ring__strip--bottom"></div>
    <svg class="ring__tab ring__tab--top"><use href="#tab-shape"/></svg>
    <svg class="ring__tab ring__tab--bottom" style="transform:scaleY(-1)"><use href="#tab-shape"/></svg>
    <p class="ring__maker">TABACO MILL DEPOT</p>
    <div class="ring__seal ring__seal--main">TM</div>
    <div class="ring__seal ring__seal--side">TM</div>
    <p class="ring__line">SLATE CREST</p>
  </section>
  <section class="ring ring--moss">
    <div class="ring__strip ring__strip--top"></div>
    <div class="ring__strip ring__strip--bottom"></div>
    <svg class="ring__tab ring__tab--top"><use href="#tab-shape"/></svg>
    <svg class="ring__tab ring__tab--bottom" style="transform:scaleY(-1)"><use href="#tab-shape"/></svg>
    <p class="ring__maker">TABACO MILL DEPOT</p>
    <div class="ring__seal ring__seal--main">TM</div>
    <div class="ring__seal ring__seal--side">TM</div>
    <p class="ring__line">MOSS CREST</p>
  </section>
  <section class="ring ring--ochre">
    <div class="ring__strip ring__strip--top"></div>
    <div class="ring__strip ring__strip--bottom"></div>
    <svg class="ring__tab ring__tab--top"><use href="#tab-shape"/></svg>
    <svg class="ring__tab ring__tab--bottom" style="transform:scaleY(-1)"><use href="#tab-shape"/></svg>
    <p class="ring__maker">TABACO MILL DEPOT</p>
    <div class="ring__seal ring__seal--main">TM</div>
    <div class="ring__seal ring__seal--side">TM</div>
    <p class="ring__line">OCHRE CREST</p>
  </section>
  <section class="ring ring--pewter">
    <div class="ring__strip ring__strip--top"></div>
    <div class="ring__strip ring__strip--bottom"></div>
    <svg class="ring__tab ring__tab--top"><use href="#tab-shape"/></svg>
    <svg class="ring__tab ring__tab--bottom" style="transform:scaleY(-1)"><use href="#tab-shape"/></svg>
    <p class="ring__maker">TABACO MILL DEPOT</p>
    <div class="ring__seal ring__seal--main">TM</div>
    <div class="ring__seal ring__seal--side">TM</div>
    <p class="ring__line">PEWTER CREST</p>
  </section>
  <section class="ring ring--amber">
    <div class="ring__strip ring__strip--top"></div>
    <div class="ring__strip ring__strip--bottom"></div>
    <svg class="ring__tab ring__tab--top"><use href="#tab-shape"/></svg>
    <svg class="ring__tab ring__tab--bottom" style="transform:scaleY(-1)"><use href="#tab-shape"/></svg>
    <p class="ring__maker">TABACO MILL DEPOT</p>
    <div class="ring__seal ring__seal--main">TM</div>
    <div class="ring__seal ring__seal--side">TM</div>
    <p class="ring__line">AMBER CREST</p>
  </section>
</main>
</body>
</html>
```